professional health club Info Flyer

we need a professional health club DL flyer that will provide information regarding our 24/7 health club services to enquiries whilst we are unstaffed. these will be placed outside on main street.

www.vitrova.club

On the reverse side, we want to offer 2 introductory specials;
1. free 7 day trial
2. Membership, classes & personal training introductory month3 personal training sessions and month 24/7 membership and classes for $99.95 (saving of over $159.85)
conditions: valid for new members only

SIZE: DL with double sided

Target Market(s)

professional, male and female of all ages (in particular those 30+)

Industry/Entity Type

Health And Wellness

Colors
33a6d7
abd037
f78f20
ffffff

Requirements
Must have
• - professional allied health feel about flyer with images
• - contact details
• - services provided include 24/7 memberships, classes, special population group training, Exercise physiology, physiotherapy, massage, nutrition, rehabilitation.
• - a catch to get them to contact us
• - our slogan "We are here to improve your quality of life"

```html
<!DOCTYPE html>
<html lang="en">
<head>
<meta charset="utf-8">
<title>Vitrova Health Club – Introductory Specials</title>
<link href="https://fonts.googleapis.com/css2?family=Arimo:ital,wght@0,400;0,700;1,700&display=swap" rel="stylesheet">
<style>
  :root {
    --navy: #2b2f78;
    --green: #abd037;
    --orange: #f78f20;
    --blue: #33a6d7;
    --blue-soft: #a9d8ee;
    --white: #ffffff;
    --shadow: rgba(0,0,0,0.28);
  }
  * { box-sizing: border-box; margin: 0; padding: 0; }
  html, body { width: 1200px; height: 2540px; overflow: hidden; background: var(--white); }
  body { font-family: "Arimo", Arial, sans-serif; color: var(--navy); }
  .flyer { position: relative; width: 1200px; height: 2540px; overflow: hidden; background: var(--white); }

  .slogan { position: absolute; left: 80px; top: 36px; width: 1060px; font-style: italic; font-weight: 700; font-size: 66px; line-height: 80px; color: var(--navy); }
  .slogan span { display: block; }
  .slogan .line-two { text-align: right; }

  .accent-square { position: absolute; }
  .accent-square.sq-a { left: 0; top: 168px; width: 160px; height: 150px; background: var(--blue-soft); opacity: .75; }
  .accent-square.sq-b { left: 84px; top: 210px; width: 190px; height: 190px; background: var(--blue-soft); opacity: .55; }
  .accent-square.sq-c { left: 960px; top: 1140px; width: 200px; height: 200px; background: var(--orange); }
  .accent-square.sq-d { left: 1010px; top: 1100px; width: 70px; height: 70px; background: var(--blue-soft); opacity: .8; }

  .photo { position: absolute; border: 14px solid var(--white); box-shadow: 0 6px 18px var(--shadow); }
  .photo.equipment { left: 432px; top: 236px; width: 790px; height: 748px; background: linear-gradient(135deg, #d9d9d9 0%, #8e8e8e 45%, #3a3a3a 100%); }
  .photo.spin-class { left: 28px; top: 864px; width: 840px; height: 784px; background: linear-gradient(120deg, #c9b9a6 0%, #7b6d63 45%, #2e2b2b 100%); }

  .trial-box { position: absolute; left: 88px; top: 312px; width: 680px; height: 510px; background: var(--green); box-shadow: 0 6px 18px var(--shadow); text-align: center; padding-top: 42px; }
  .trial-box .free { font-size: 196px; line-height: 190px; font-weight: 400; color: var(--navy); letter-spacing: 2px; }
  .trial-box .trial { font-size: 92px; line-height: 104px; font-weight: 400; color: var(--white); }
  .trial-box .special { font-size: 54px; line-height: 70px; color: var(--navy); }

  .offer-box { position: absolute; left: 400px; top: 1320px; width: 800px; height: 880px; background: var(--white); border: 14px solid var(--orange); border-right: none; box-shadow: 0 6px 18px var(--shadow); padding: 56px 30px 0 48px; }
  .offer-box .price { font-size: 196px; line-height: 196px; color: var(--navy); }
  .offer-box .saving { font-size: 38px; line-height: 50px; color: var(--navy); margin: 6px 0 30px 10px; }
  .offer-box .package { font-size: 60px; line-height: 72px; font-weight: 700; color: var(--orange); }
  .offer-box .conditions { font-size: 34px; line-height: 48px; color: var(--navy); margin-top: 18px; }

  .contact { position: absolute; left: 80px; top: 2170px; width: 700px; color: var(--navy); }
  .contact h2 { font-size: 60px; line-height: 76px; font-weight: 700; margin-bottom: 8px; }
  .contact p { font-size: 40px; line-height: 50px; }
  .contact .row { display: flex; align-items: center; gap: 22px; margin-top: 14px; }
  .contact .row svg { width: 42px; height: 42px; flex: none; }

  .corner-mosaic { position: absolute; left: 800px; top: 2214px; width: 400px; height: 326px; background: linear-gradient(135deg, rgba(255,255,255,0) 0%, rgba(169,216,238,.7) 30%, rgba(51,166,215,.7) 55%, rgba(171,208,55,.7) 75%, rgba(247,143,32,.7) 100%); }
</style>
</head>
<body>
<main class="flyer">
  <div class="accent-square sq-a"></div>
  <div class="accent-square sq-b"></div>

  <h1 class="slogan"><span>We are here to improve</span><span class="line-two">your quality of life</span></h1>

  <div class="photo equipment" role="img" aria-label="Row of cross-trainer machines in the gym"></div>

  <section class="trial-box">
    <div class="free">FREE</div>
    <div class="trial">7 Day Trial</div>
    <div class="special">Introductory Special</div>
  </section>

  <div class="photo spin-class" role="img" aria-label="Members riding bikes in an indoor cycling class"></div>

  <div class="accent-square sq-d"></div>
  <div class="accent-square sq-c"></div>

  <section class="offer-box">
    <div class="price">$99.95</div>
    <div class="saving">(saving of over $159.85)</div>
    <div class="package">Membership, Classes<br>&amp; Personal Training<br>Introductory Month</div>
    <div class="conditions">Conditions: Valid for new members only</div>
  </section>

  <div class="corner-mosaic" role="img" aria-label="Decorative mosaic of blue, green and orange squares"></div>

  <section class="contact">
    <h2>Contact Us</h2>
    <p>52 Larkin Street, Bellmere<br>Sydney NSW 2199</p>
    <div class="row">
      <svg viewBox="0 0 24 24" aria-hidden="true"><path fill="#2b2f78" d="M6.6 10.8a15.1 15.1 0 0 0 6.6 6.6l2.2-2.2a1 1 0 0 1 1-.25 11.4 11.4 0 0 0 3.6.57 1 1 0 0 1 1 1V20a1 1 0 0 1-1 1A17 17 0 0 1 3 4a1 1 0 0 1 1-1h3.5a1 1 0 0 1 1 1c0 1.25.2 2.45.57 3.57a1 1 0 0 1-.25 1z"/></svg>
      <p>+612 80001234</p>
    </div>
    <div class="row">
      <svg viewBox="0 0 24 24" aria-hidden="true"><rect x="2.5" y="5" width="19" height="14" fill="none" stroke="#2b2f78" stroke-width="2"/><path d="M3 6l9 7 9-7" fill="none" stroke="#2b2f78" stroke-width="2"/></svg>
      <p>hello@vitrova.club</p>
    </div>
  </section>
</main>
</body>
</html>
```